Wedding Music Playlist Template

Hi, I'm a wedding musician and I'd like a 1 pager wedding music template created. It needs to be editable for future weddings.

At the top of the template:
Bride First Name & Groom First Name plus 's WEDDING
Date of Wedding:
Venue name:

(The form needs to be flexible where I can remove/interchange Prelude Ceremony / Ceremony / Canapes / Reception) as sometimes I will play music just for a Ceremony sometimes for both Ceremony/Canapes or sometimes just the reception only or all of the above.

Section 1: Prelude Ceremony (this could be up to 5 songs)

Section 2: Ceremony
Processional (this is sometimes 1 or 2 songs)
Signing of Papers (this is sometimes 1 or 2 songs)
Recessional (1 song)

Section 3: Canapes

Section 4: Reception

Within each section
Artist
Song

I'd also like the template to feature
logo (attached) and social media links
website URL tomwelker.com.au
instagram: tomwelkertunes
facebook: tomwelkerkeysman
soundcloud: keysguy_ceremonies

I see the form/template serving two purposes.
1) I'll send back to the bride when she books me for a wedding and she may socialise it.
2) Posting on instagram as I perform at each wedding and attract engaged brides looking for wedding pianist or even just ideas for wedding music.

Target Market(s)

Engaged Couples looking for wedding music or suggested music for wedding

Industry/Entity Type

Wedding

Requirements
Must have
• Please see project description.
Nice to have
• Background wedding image with text overlayed

```html
<!DOCTYPE html>
<html lang="en">
<head>
<meta charset="utf-8">
<title>Clara &amp; James's Wedding – Music Programme</title>
<link href="https://fonts.googleapis.com/css2?family=Great+Vibes&family=Tinos:wght@400;700&family=Open+Sans:wght@400;700&display=swap" rel="stylesheet">
<style>
  :root {
    --backdrop: #f4f4f2;
    --paper: #ffffff;
    --teal: #1aa79b;
    --ink: #2b2b2b;
    --ink-soft: #555555;
    --photo-light: #e9e7e6;
    --photo-mid: #c9c4c3;
    --photo-blush: #e6cfcd;
    --photo-dark: #8d8887;
  }
  * { box-sizing: border-box; margin: 0; padding: 0; }
  html, body {
    width: 1200px; height: 900px; overflow: hidden;
    background: var(--backdrop);
  }
  .flyer {
    position: absolute; left: 296px; top: 20px;
    width: 608px; height: 860px;
    background: var(--paper);
    box-shadow: 0 6px 24px rgba(0,0,0,0.10);
    overflow: hidden;
    font-family: "Tinos", "Times New Roman", serif;
    color: var(--ink);
  }
  .hero { position: absolute; left: 0; top: 0; width: 608px; height: 340px; }
  .brand {
    position: absolute; left: 28px; top: 64px;
    display: flex; align-items: center; gap: 8px;
    font-family: "Open Sans", Arial, sans-serif;
    font-size: 13px; font-weight: 700; letter-spacing: 0.5px;
    color: var(--ink);
  }
  .brand-dot { width: 30px; height: 30px; border-radius: 50%; background: #111; }
  .programme {
    position: absolute; left: 0; right: 0; top: 318px;
    text-align: center;
  }
  .couple {
    font-family: "Great Vibes", cursive;
    color: var(--teal);
    font-size: 66px; line-height: 1;
    font-weight: 400;
  }
  .couple .suffix { font-size: 36px; vertical-align: 18px; margin-left: 4px; }
  .date { font-size: 17px; letter-spacing: 0.5px; margin-top: 6px; }
  .date sup { font-size: 10px; }
  .venue {
    font-size: 18px; letter-spacing: 0.5px; margin-top: 2px;
    display: flex; justify-content: center; align-items: center; gap: 6px;
  }
  .pin { width: 12px; height: 16px; }
  .section-title { font-size: 13px; letter-spacing: 0.3px; margin-top: 10px; }
  .part { font-size: 12px; color: var(--ink); margin-top: 2px; }
  .song-list { list-style: none; }
  .song {
    font-family: "Great Vibes", cursive;
    font-size: 15px; line-height: 19px; color: var(--ink-soft);
  }
  .song::before { content: "\266A"; color: var(--teal); font-family: "Tinos", serif; font-size: 11px; margin-right: 6px; }
  .contacts {
    position: absolute; left: 24px; right: 24px; bottom: 34px;
    display: flex; justify-content: space-between;
    font-family: "Open Sans", Arial, sans-serif;
    font-size: 11px; color: var(--ink);
  }
  .contact { display: flex; align-items: center; gap: 6px; }
  .contact-dot { width: 12px; height: 12px; border-radius: 50%; background: var(--teal); }
</style>
</head>
<body>
  <main class="flyer">
    <svg class="hero" viewBox="0 0 608 340" role="img" aria-label="Photograph of a pale pink rose bridal bouquet beside white bridal heels on a white wooden floor with a wedding gown behind">
      <defs>
        <linearGradient id="heroTone" x1="0" y1="0" x2="1" y2="1">
          <stop offset="0" stop-color="var(--photo-light)"/>
          <stop offset="0.35" stop-color="var(--photo-blush)"/>
          <stop offset="0.7" stop-color="var(--photo-mid)"/>
          <stop offset="1" stop-color="var(--photo-dark)"/>
        </linearGradient>
      </defs>
      <path d="M0 0 H608 V250 C520 300 420 330 300 322 C190 315 90 300 0 305 Z" fill="url(#heroTone)"/>
    </svg>

    <div class="brand"><span class="brand-dot"></span>TOMWELKER</div>

    <section class="programme">
      <h1 class="couple">Clara &amp; James<span class="suffix">'s Wedding</span></h1>
      <p class="date">SAT August 26<sup>th</sup> 2017</p>
      <p class="venue">
        <svg class="pin" viewBox="0 0 12 16"><path d="M6 0C2.7 0 0 2.6 0 5.8 0 10 6 16 6 16s6-6 6-10.2C12 2.6 9.3 0 6 0zm0 8.2A2.4 2.4 0 1 1 6 3.4a2.4 2.4 0 0 1 0 4.8z" fill="var(--teal)"/></svg>
        WILLOW CREEK ESTATE
      </p>

      <h2 class="section-title">SECTION 1: PRELUDE CEREMONY</h2>
      <ul class="song-list">
        <li class="song">Air (Handel)</li>
        <li class="song">Amazing Grace</li>
        <li class="song">Arioso (Bach)</li>
        <li class="song">Ave Maria (Schubert)</li>
        <li class="song">Canon in D (Pachelbel)</li>
      </ul>

      <h2 class="section-title">SECTION 2: CEREMONY</h2>
      <p class="part">- Processional</p>
      <ul class="song-list"><li class="song">Trumpet Tune (Purcell) &amp; Trumpet Voluntary (Clark)</li></ul>
      <p class="part">- Signing of Papers</p>
      <ul class="song-list"><li class="song">Old Irish Blessing</li></ul>
      <p class="part">- Recessional</p>
      <ul class="song-list"><li class="song">Jesu, Joy of Man's Desiring (Bach)</li></ul>

      <h2 class="section-title">SECTION 3: CANAPES</h2>
      <h2 class="section-title">SECTION 4: RECEPTION</h2>
    </section>

    <footer class="contacts">
      <span class="contact"><span class="contact-dot"></span>http://tomwelker.com.au/</span>
      <span class="contact"><span class="contact-dot"></span>tomwelkertunes</span>
      <span class="contact"><span class="contact-dot"></span>tomwelkerkeysman</span>
      <span class="contact"><span class="contact-dot"></span>keysguy_ceremonies</span>
    </footer>
  </main>
</body>
</html>
```